Solar energy proposal for homeowners

I am providing households with solar energy proposals, and I need a high-quality brochure that is packaged cleverly to attract the homeowner's attention. Take a look at the one page solar brochure that I have included to get an idea of text and content.

Target Market(s)

Residential Homeowners

Industry/Entity Type

Solar

Requirements
Must have
• High quality document

```html
<!DOCTYPE html>
<html lang="en">
<head>
<meta charset="utf-8">
<title>Brightvale Energy – Solar for $0 Down</title>
<link rel="stylesheet" href="https://fonts.googleapis.com/css2?family=Archivo:wght@800;900&family=Poppins:wght@400;500;600;700&display=swap">
<style>
  :root {
    --navy-deep: #0a1f4a;
    --navy: #0c2e6e;
    --navy-text: #0b2a5c;
    --glow: #1456b8;
    --cyan: #14c3e6;
    --aqua: #2fd6c8;
    --lime: #b4e21e;
    --pill: #1c4a93;
    --white: #ffffff;
    --ink: #1b2233;
    --stop: #e0262b;
    --page-bg: #ffffff;
  }
  * { box-sizing: border-box; margin: 0; padding: 0; }
  html, body { width: 1200px; height: 1200px; overflow: hidden; background: var(--page-bg); }
  body { font-family: "Poppins", sans-serif; }

  .flyer {
    position: absolute; left: 136px; top: 0; width: 928px; height: 1200px; overflow: hidden;
    background:
      radial-gradient(ellipse 420px 380px at 330px 420px, var(--glow) 0%, rgba(20,86,184,0) 100%),
      linear-gradient(180deg, var(--navy-deep) 0%, var(--navy) 100%);
  }
  .abs { position: absolute; }

  /* brand */
  .brand { left: 74px; top: 56px; display: flex; align-items: center; gap: 14px; }
  .brand-square { width: 50px; height: 50px; background: var(--cyan); border-radius: 6px; }
  .brand-name { font-family: "Poppins", sans-serif; font-weight: 500; font-size: 40px; color: var(--aqua); line-height: 1; letter-spacing: 0.5px; }
  .brand-sub { display: block; font-size: 14px; letter-spacing: 1px; text-align: right; margin-top: 4px; }

  /* headline */
  .icon-rail {
    left: 74px; top: 162px; width: 40px; height: 178px; border-radius: 20px;
    background: linear-gradient(180deg, var(--cyan), var(--lime)); padding: 4px;
  }
  .icon-rail-inner { width: 100%; height: 100%; border-radius: 16px; background: var(--navy-deep); position: relative; }
  .rail-dot { position: absolute; left: 3px; width: 26px; height: 26px; border-radius: 50%; background: var(--white); }
  .rail-dot::after { content: ""; position: absolute; inset: 7px; border-radius: 50%; background: var(--navy-deep); }

  .headline { left: 129px; top: 158px; font-family: "Archivo", sans-serif; font-weight: 900; font-size: 45px; line-height: 46px; color: var(--white); letter-spacing: 0.3px; white-space: nowrap; }
  .headline .line { display: block; height: 46px; }
  .headline .dollar { font-size: 24px; position: relative; top: -16px; margin-right: 1px; }
  .headline .accent {
    background: linear-gradient(90deg, var(--cyan), var(--lime));
    -webkit-background-clip: text; background-clip: text; color: transparent;
  }
  .tagline { left: 76px; top: 348px; font-size: 19.5px; font-weight: 500; color: var(--white); white-space: nowrap; }
  .tagline strong { font-weight: 700; }

  /* about column */
  .about { left: 570px; top: 66px; width: 285px; }
  .section-title {
    font-family: "Archivo", sans-serif; font-weight: 900; font-size: 22px; letter-spacing: 0.3px;
    background: linear-gradient(90deg, var(--aqua), var(--lime));
    -webkit-background-clip: text; background-clip: text; color: transparent;
  }
  .about p { color: var(--white); font-size: 12px; line-height: 14.6px; margin-top: 6px; }
  .why { margin-top: 22px; }
  .perk-list { list-style: none; margin-top: 10px; }
  .perk {
    width: 266px; height: 20px; border-radius: 10px; background: var(--pill); margin-bottom: 5.8px;
    display: flex; align-items: center; gap: 5px; padding-left: 10px; color: var(--white); font-size: 12px;
  }
  .perk strong { font-weight: 700; }

  /* photo area */
  .hero-photo { left: 0; top: 380px; }

  /* services */
  .services-title {
    left: 0; top: 850px; width: 928px; display: flex; justify-content: center; align-items: center; gap: 8px;
    font-family: "Archivo", sans-serif; font-weight: 900; font-size: 25px; color: var(--navy-text);
  }
  .services-title::before, .services-title::after { content: ""; width: 92px; height: 1.5px; background: var(--navy-text); }
  .card {
    top: 918px; width: 184px; height: 162px; border-radius: 14px;
    background: rgba(255,255,255,0.45); text-align: center; padding-top: 36px;
  }
  .card-icon {
    position: absolute; left: 68px; top: -24px; width: 48px; height: 48px; border-radius: 50%;
    background: var(--navy-text); border: 3px solid var(--cyan);
    display: flex; align-items: center; justify-content: center;
  }
  .card h3 { font-family: "Archivo", sans-serif; font-weight: 800; font-size: 16px; line-height: 20px; color: var(--navy-text); letter-spacing: 0.3px; }
  .card p { font-size: 12.4px; line-height: 14.6px; color: var(--navy-text); margin-top: 3px; padding: 0 22px; }

  /* footer */
  .contact {
    left: 0; top: 1101px; width: 928px; height: 99px; background: var(--white);
    display: flex; align-items: center; justify-content: center; gap: 22px;
    font-size: 16.5px; color: var(--ink); letter-spacing: 0.3px; padding-bottom: 24px;
  }
  .contact span { display: flex; align-items: center; gap: 7px; }
</style>
</head>
<body>
<main class="flyer">

  <svg class="abs" width="928" height="1101" viewBox="0 0 928 1101" style="left:0;top:0">
    <defs>
      <linearGradient id="bandFill" x1="0" y1="0" x2="0" y2="1">
        <stop offset="0" stop-color="#0fbfe8"/>
        <stop offset="0.55" stop-color="#7ee3b8"/>
        <stop offset="1" stop-color="#b2e01c"/>
      </linearGradient>
    </defs>
    <polygon points="0,865 928,783 928,1101 0,1101" fill="url(#bandFill)"/>
  </svg>

  <div class="abs brand">
    <span class="brand-square"></span>
    <span class="brand-name">brightvale<span class="brand-sub">ENERGY</span></span>
  </div>

  <div class="abs icon-rail">
    <div class="icon-rail-inner">
      <span class="rail-dot" style="top:22px"></span>
      <span class="rail-dot" style="top:84px"></span>
      <span class="rail-dot" style="top:138px"></span>
    </div>
  </div>

  <h1 class="abs headline">
    <span class="line">SOLAR FOR</span>
    <span class="line"><span class="dollar">$</span>0 DOWN.</span>
    <span class="line accent">NO LIENS.</span>
    <span class="line accent">NO KIDDING.</span>
  </h1>
  <p class="abs tagline">Power Your Future with <strong>Brightvale Energy</strong></p>

  <section class="abs about">
    <h2 class="section-title">ABOUT US</h2>
    <p>At Brightvale Energy, our masion is to make solar simple and accessible for everyone. No high-pressure sales-just the information you need to make smart choice With our solar rental program, you can lower your monthly energy costs and pay less than your current eleconcity bill.</p>
    <h2 class="section-title why">WHY CHOOSE US?</h2>
    <ul class="perk-list">
      <li class="perk"><svg width="12" height="12" viewBox="0 0 12 12"><circle cx="6" cy="6" r="5" fill="none" stroke="var(--stop)" stroke-width="1.4"/><line x1="2.6" y1="9.4" x2="9.4" y2="2.6" stroke="var(--stop)" stroke-width="1.4"/></svg><span><strong>No</strong> Tinanong</span></li>
      <li class="perk"><svg width="12" height="12" viewBox="0 0 12 12"><circle cx="6" cy="6" r="5" fill="none" stroke="var(--stop)" stroke-width="1.4"/><line x1="2.6" y1="9.4" x2="9.4" y2="2.6" stroke="var(--stop)" stroke-width="1.4"/></svg><span><strong>No</strong> liens</span></li>
      <li class="perk"><svg width="12" height="12" viewBox="0 0 12 12"><circle cx="6" cy="6" r="5" fill="none" stroke="var(--stop)" stroke-width="1.4"/><line x1="2.6" y1="9.4" x2="9.4" y2="2.6" stroke="var(--stop)" stroke-width="1.4"/></svg><span><strong>No</strong> down payment</span></li>
      <li class="perk"><svg width="12" height="12" viewBox="0 0 12 12"><circle cx="6" cy="6" r="5" fill="none" stroke="var(--stop)" stroke-width="1.4"/><line x1="2.6" y1="9.4" x2="9.4" y2="2.6" stroke="var(--stop)" stroke-width="1.4"/></svg><span><strong>No</strong> insurance costs</span></li>
      <li class="perk"><svg width="12" height="12" viewBox="0 0 12 12"><circle cx="6" cy="6" r="5" fill="none" stroke="var(--stop)" stroke-width="1.4"/><line x1="2.6" y1="9.4" x2="9.4" y2="2.6" stroke="var(--stop)" stroke-width="1.4"/></svg><span><strong>No</strong> long term commitment</span></li>
      <li class="perk"><svg width="12" height="12" viewBox="0 0 12 12"><circle cx="6" cy="6" r="5" fill="none" stroke="var(--stop)" stroke-width="1.4"/><line x1="2.6" y1="9.4" x2="9.4" y2="2.6" stroke="var(--stop)" stroke-width="1.4"/></svg><span><strong>No</strong> maintenance costs</span></li>
    </ul>
  </section>

  <svg class="abs hero-photo" width="928" height="490" viewBox="0 0 928 490" role="img" aria-label="Photo of a modern two-storey white house with rooftop solar panels, warmly lit windows, a glass garage door and a landscaped green garden at dusk">
    <defs>
      <linearGradient id="heroFill" x1="0" y1="0" x2="0" y2="1">
        <stop offset="0" stop-color="#1f63bd" stop-opacity="0"/>
        <stop offset="0.18" stop-color="#2a6cc2" stop-opacity="0.55"/>
        <stop offset="0.42" stop-color="#dfe7ef"/>
        <stop offset="0.6" stop-color="#f3e3bd"/>
        <stop offset="0.78" stop-color="#78ae4c"/>
        <stop offset="0.92" stop-color="#4f8f3a"/>
        <stop offset="1" stop-color="#c6d0d6"/>
      </linearGradient>
    </defs>
    <polygon points="0,30 928,30 928,403 0,485" fill="url(#heroFill)"/>
    <line x1="0" y1="485" x2="928" y2="403" stroke="var(--navy-deep)" stroke-width="3"/>
  </svg>

  <h2 class="abs services-title">OUR BEST SERVICE</h2>

  <article class="abs card" style="left:69px">
    <span class="card-icon"><svg width="22" height="22" viewBox="0 0 22 22"><circle cx="11" cy="8" r="5" fill="none" stroke="#fff" stroke-width="2"/><path d="M3 19 Q11 13 19 19" fill="none" stroke="#fff" stroke-width="2"/></svg></span>
    <h3>AFFORDABLE &amp;<br>TRANSPARENT</h3>
    <p>Simple pricing, no hidden fees and a fixed monthly rate lower than typical energy bills.</p>
  </article>
  <article class="abs card" style="left:270px">
    <span class="card-icon"><svg width="22" height="22" viewBox="0 0 22 22"><path d="M11 20 C4 12 4 9 4 8 a7 7 0 0 1 14 0 c0 1 0 4 -7 12z" fill="none" stroke="#fff" stroke-width="2"/><circle cx="11" cy="8" r="2.5" fill="#fff"/></svg></span>
    <h3>LOCAL<br>EXPERTISE</h3>
    <p>Florida-based team that understands the needs of Orlando and stateside homeowners.</p>
  </article>
  <article class="abs card" style="left:471px">
    <span class="card-icon"><svg width="22" height="22" viewBox="0 0 22 22"><circle cx="11" cy="11" r="7" fill="none" stroke="#fff" stroke-width="2.5" stroke-dasharray="4 2.5"/><circle cx="11" cy="11" r="2.5" fill="#fff"/></svg></span>
    <h3>EXPERT<br>INSTALLATION</h3>
    <p>Certified professionals handle installation, maintenance, and repars end to end.</p>
  </article>
  <article class="abs card" style="left:671px">
    <span class="card-icon"><svg width="22" height="22" viewBox="0 0 22 22"><path d="M11 3 L17 13 H5 Z" fill="none" stroke="#fff" stroke-width="2"/><path d="M4 17 H18" stroke="#fff" stroke-width="2"/></svg></span>
    <h3>ECO<br>FRIENDLY</h3>
    <p>Clean, renewable solar energy that helps reduce your cartion footprint.</p>
  </article>

  <footer class="abs contact">
    <span><svg width="18" height="18" viewBox="0 0 18 18"><path d="M4 2 L7 2 L8 6 L6 7.5 Q8 11 10.5 12 L12 10 L16 11 L16 14 Q15 16 13 16 Q3 14 2 4 Q2 2 4 2z" fill="var(--cyan)"/></svg>407.555.0142</span>
    <span><svg width="14" height="18" viewBox="0 0 14 18"><path d="M7 17 C1 10 1 8 1 7 a6 6 0 0 1 12 0 c0 1 0 3 -6 10z" fill="var(--cyan)"/><circle cx="7" cy="7" r="2.2" fill="#fff"/></svg>1280 Cedar Grove Lane Orlando, FL 32801</span>
    <span><svg width="17" height="17" viewBox="0 0 17 17"><circle cx="8.5" cy="8.5" r="7" fill="none" stroke="var(--cyan)" stroke-width="1.5"/><ellipse cx="8.5" cy="8.5" rx="3" ry="7" fill="none" stroke="var(--cyan)" stroke-width="1.3"/><line x1="1.5" y1="8.5" x2="15.5" y2="8.5" stroke="var(--cyan)" stroke-width="1.3"/></svg>www.brightvaleenergy.com</span>
  </footer>

</main>
</body>
</html>
```